120ml Jar Label — Masculine Cosmetic Foot Balm for Cracked, Hardworking Heels

We need a print-ready wraparound label for a 120ml jar — a brown/amber glass jar with a black metal screw lid (file photo attached).

--DO NOT PUT A BARCODE ON THE LABEL PLEASE--
**PLEASE READ "PLAN HUDDLE PROJECT BRIEF FINAL.MD" IN ATTACHED FILES IF YOU ARE SUBMITTING A DESIGN.**

The label is 190mm wide × 40mm high.
We need files to be in an .ai format with a 2mm bleed at the end.
Social media handle: @bramblekeepnz (facebook, instagram and tiktok)

Bramble Keep is a New Zealand foot-care brand making practical, no-nonsense products for hardworking men whose jobs wreck their feet. Our flagship product, Ridge Mender Balm, helps fix thick, cracked, hardworking skin.

Brand color scheme and overview is all in the brief file. You may add some brand aligned colors outside of the specified hex codes as you see fit to make a great design. Feel free to remove the "Bramble Keep" text from the logo so Bramble Keep is not doubled up on the front of the label

The tone we want: direct, rugged, and credible — like a workwear brand, not a spa brand. Most cracked-heel products on the market lean soft and feminine; we want to stand apart by looking like a serious fix for a real problem, made in New Zealand.

Full legal requirements for New Zealand cosmetic labelling (ingredients, directions, net contents, origin, etc.) are listed in the attached brief document — these are non-negotiable and must stay legible.

Please see the label attached "Label spacing guide" for this project's rough spacing guide. This label is the same size and sits well on the jar. This label doesn't need to be spaced quite as much as the Verin Label

I want to run the design for a week - I feel 7 days is a good amount of time for designers to see the work, digest the brief and create something remarkable and memorable for Bramble Keep.

Target Market(s)

Working men in New Zealand whose jobs or lifestyle put heavy wear on their feet — tradies, farmers, hospital/shift workers, hunters, and outdoors people. Practical, value-driven buyers rather than luxury skincare shoppers.

Industry/Entity Type

Beauty / Health & Wellness / Cosmetics

Font styles to use
Sans Serif
Other font styles liked:
• Montserrat (bold, headings), Inter (regular, body)

Colors
00AB8E
00BBA5
67D7C9
C6EFE9
E9F9F6
FFC000
F8CF3A
FAE287
FDF2CF
FEFAEE

Requirements
Must have
• All NZ cosmetic labelling requirements from the attached brief (product name, tag line, net contents, ingredients, directions, storage, made in NZ) — legible and complete, not omitted for aesthetics Fits 190mm × 40mm wraparound format for a 120ml brown jar with black lid Uses our existing brand colors: Deep Olive #3C4A34, Bone White #F4EFE6, Terracotta Clay #C1683D, and Warm Grey #4A4540 (exact palette in attached brief) Uses Montserrat (headings) and Inter (body) or close equivalents Incorporates our existing shield-and-wing logo (attached) Brand name and product name clearly readable from a normal shelf/bathroom-cabinet distance
Nice to have
• A style that could extend into a hero/product photo later, similar to the NZ-hills-backdrop look on our website (screenshot attached) — not required for the label itself, just good to keep in mind Original icon work (e.g. a small soak/apply/sock icon set) if it fits the rugged brand feel A design that could work as a small back-label/wraparound split if the front can't fit everything at a readable size
Should not have
• No pastel colors, floral motifs, or delicate script fonts — this should never look like spa/luxury skincare. Don't introduce new brand colors outside the palette provided other than black.

```html
<!DOCTYPE html>
<html lang="en">
<head>
<meta charset="utf-8">
<title>Bramble Keep — Ridge Mender Balm label options</title>
<link href="https://fonts.googleapis.com/css2?family=Barlow+Condensed:wght@400;500;600;700;800&family=Barlow+Semi+Condensed:wght@400;500;600&family=Montserrat:wght@700;800&family=Patrick+Hand&display=swap" rel="stylesheet">
<style>
  :root {
    --olive-dark: #2b2f27;
    --bone: #f3ede5;
    --clay: #b9643c;
    --clay-light: #c9774c;
    --ink: #2a2a28;
    --grey: #4a4540;
    --hill-1: #4a5a3c;
    --hill-2: #6b7660;
    --page: #ffffff;
  }
  * { box-sizing: border-box; margin: 0; padding: 0; }
  html, body { width: 1200px; height: 1004px; overflow: hidden; background: var(--page); }
  .sheet { position: relative; width: 1200px; height: 1004px; font-family: "Barlow Semi Condensed", sans-serif; color: var(--ink); }

  .option-title { position: absolute; left: 66px; font-family: "Montserrat", sans-serif; font-weight: 800; font-size: 24px; letter-spacing: 1.5px; color: var(--clay); }
  .option-note { font-family: "Patrick Hand", cursive; font-weight: 400; font-size: 23px; letter-spacing: 0.3px; color: var(--ink); margin-left: 14px; }

  .label { position: absolute; left: 66px; width: 1080px; height: 227px; border-radius: 9px; overflow: hidden; background: var(--bone); border: 1px solid #e4ddd2; }
  .label--dark { background: var(--olive-dark); border: none; }
  .label > * { position: absolute; }
  .label-bg { left: 0; top: 0; width: 1080px; height: 227px; }

  .kicker { font-family: "Barlow Condensed", sans-serif; font-weight: 600; color: var(--clay); font-size: 12.5px; letter-spacing: 0.2px; }
  .body-copy { font-size: 11.6px; line-height: 14.4px; }
  .body-copy--light { color: var(--bone); }
  .justify { text-align: justify; }

  .brand-name { font-family: "Barlow Condensed", sans-serif; font-weight: 700; color: var(--bone); letter-spacing: 0.5px; white-space: nowrap; }
  .brand-name sup { font-size: 0.3em; vertical-align: top; position: relative; top: 0.3em; }
  .rule { height: 1px; background: var(--clay); }
  .product-main { font-family: "Barlow Condensed", sans-serif; font-weight: 800; color: var(--bone); line-height: 0.86; white-space: nowrap; }
  .product-sub { font-family: "Barlow Condensed", sans-serif; font-weight: 800; color: var(--clay); line-height: 0.9; white-space: nowrap; }
  .tag-pill { background: var(--clay); color: var(--bone); font-family: "Barlow Condensed", sans-serif; font-weight: 600; font-size: 13px; letter-spacing: 0.8px; display: flex; align-items: center; justify-content: center; clip-path: polygon(3% 0, 97% 0, 100% 50%, 97% 100%, 3% 100%, 0 50%); white-space: nowrap; }
  .net { font-family: "Barlow Semi Condensed", sans-serif; font-weight: 500; color: var(--bone); font-size: 15px; white-space: nowrap; }

  .hero-art { border-radius: 10px; background: linear-gradient(160deg, #efe2cc 0%, #c9774c 55%, #4a4540 100%); }
  .origin-seal { border-radius: 50%; border: 2px solid var(--bone); background: var(--olive-dark); box-shadow: inset 0 0 0 4px var(--olive-dark), inset 0 0 0 5px var(--clay); }
  .fern-art { background: linear-gradient(200deg, var(--clay-light), var(--clay)); }
  .hills-art { background: linear-gradient(180deg, var(--olive-dark) 0%, #3d4733 40%, var(--hill-2) 70%, var(--hill-1) 100%); }

  .step { text-align: center; }
  .step-icon { display: block; margin: 0 auto; background: transparent; }
  .step-name { font-family: "Barlow Condensed", sans-serif; font-weight: 700; color: var(--clay); font-size: 12px; margin-top: 4px; }
  .step-text { font-size: 10.6px; line-height: 11.5px; }
  .step-divider { width: 1px; height: 80px; background: var(--clay); }

  .pao { width: 30px; height: 22px; border: 1.5px solid currentColor; border-radius: 3px; font-family: "Barlow Condensed", sans-serif; font-weight: 700; font-size: 9px; display: flex; align-items: flex-end; justify-content: center; padding-bottom: 2px; }
  .recycle { width: 28px; height: 26px; }

  .brand-column { text-align: center; }
  .brand-lockup { display: flex; flex-direction: column; align-items: center; }
  .brand-dot { width: 34px; height: 34px; border-radius: 50%; background: var(--olive-dark); margin-bottom: 5px; }
  .brand-word { font-family: "Barlow Condensed", sans-serif; font-weight: 700; font-size: 13px; color: var(--ink); letter-spacing: 0.3px; white-space: nowrap; }
  .maker { font-family: "Barlow Condensed", sans-serif; font-weight: 700; font-size: 11px; line-height: 12px; }
  .maker small { display: block; width: 80px; margin: 2px auto 0; white-space: normal; font-family: "Barlow Semi Condensed", sans-serif; font-weight: 500; font-size: 8.5px; line-height: 11px; }
  .social-row { display: flex; gap: 6px; justify-content: center; }
  .social-row span { width: 15px; height: 15px; border-radius: 50%; border: 1.2px solid var(--ink); }
  .handle, .web { font-family: "Barlow Condensed", sans-serif; font-weight: 600; font-size: 9.5px; white-space: nowrap; }
  .made-in { font-family: "Barlow Condensed", sans-serif; font-weight: 600; color: var(--clay); font-size: 10px; line-height: 11.5px; letter-spacing: 0.4px; }
  .col-rule { background: var(--clay); height: 1px; }
  .col-vrule { background: var(--clay); width: 1px; }

  .footnote { position: absolute; left: 68px; top: 916px; font-family: "Patrick Hand", cursive; font-size: 23px; color: #55554f; letter-spacing: 0.4px; }
  .footnote b { color: #3a3a36; }
</style>
</head>
<body>
<main class="sheet">

  <!-- OPTION 4 -->
  <h2 class="option-title" style="top:28px;">OPTION 4</h2>
  <section class="label label--dark" style="top:63px;">
    <div class="hills-art" role="img" aria-label="Illustrated New Zealand hills with a winding farm track" style="left:650px;top:80px;width:210px;height:147px;"></div>
    <svg class="label-bg" viewBox="0 0 1080 227" aria-hidden="true">
      <path d="M854 0 L1080 0 L1080 227 L854 227 L857 215 L852 203 L858 190 L851 176 L857 162 L852 148 L858 134 L851 120 L857 106 L852 92 L858 78 L851 64 L857 50 L852 36 L858 22 L852 10 Z" fill="var(--bone)"/>
    </svg>

    <p class="kicker" style="left:27px;top:24px;font-size:12px;">DIRECTIONS:</p>
    <p class="body-copy body-copy--light" style="left:27px;top:38px;width:200px;">Soak feet in warm water. Dry thoroughly. Massage a generous amount into heels. For results, use nightly and wear socks.</p>
    <div class="step" style="left:27px;top:88px;width:40px;">
      <svg class="step-icon" width="38" height="38" viewBox="0 0 38 38"><circle cx="19" cy="19" r="18" fill="none" stroke="var(--bone)" stroke-width="1.2"/><path d="M9 24 q3 -2 6 0 t6 0 t6 0 t3 0" fill="none" stroke="var(--bone)" stroke-width="1.2"/><path d="M9 28 q3 -2 6 0 t6 0 t6 0 t3 0" fill="none" stroke="var(--bone)" stroke-width="1.2"/></svg>
      <p class="step-name" style="color:var(--bone);font-size:9px;margin-top:6px;">SOAK</p>
    </div>
    <svg style="left:75px;top:102px;" width="8" height="10" viewBox="0 0 8 10"><path d="M1 1 L6 5 L1 9" fill="none" stroke="var(--clay)" stroke-width="2"/></svg>
    <div class="step" style="left:91px;top:88px;width:40px;">
      <svg class="step-icon" width="38" height="38" viewBox="0 0 38 38"><circle cx="19" cy="19" r="18" fill="none" stroke="var(--bone)" stroke-width="1.2"/><ellipse cx="25" cy="25" rx="4" ry="2.5" fill="none" stroke="var(--bone)" stroke-width="1.2"/></svg>
      <p class="step-name" style="color:var(--bone);font-size:9px;margin-top:6px;">APPLY</p>
    </div>
    <svg style="left:139px;top:102px;" width="8" height="10" viewBox="0 0 8 10"><path d="M1 1 L6 5 L1 9" fill="none" stroke="var(--clay)" stroke-width="2"/></svg>
    <div class="step" style="left:152px;top:88px;width:46px;">
      <svg class="step-icon" width="38" height="38" viewBox="0 0 38 38"><circle cx="19" cy="19" r="18" fill="none" stroke="var(--bone)" stroke-width="1.2"/><path d="M17 9 h7 v12 l-5 6 h-6 a3 3 0 0 1 0 -6 l4 -3 z" fill="none" stroke="var(--bone)" stroke-width="1.2"/></svg>
      <p class="step-name" style="color:var(--bone);font-size:9px;margin-top:6px;">PROTECT</p>
    </div>
    <p class="body-copy body-copy--light" style="left:27px;top:160px;white-space:nowrap;"><span class="kicker">STORAGE:</span>&nbsp; Keep out of direct sunlight.</p>
    <div class="pao" style="left:30px;top:185px;color:var(--bone);">6M</div>
    <svg class="recycle" style="left:84px;top:183px;" viewBox="0 0 28 26"><path d="M14 3 L25 22 L3 22 Z" fill="none" stroke="var(--bone)" stroke-width="1.6" stroke-dasharray="9 3"/></svg>

    <div class="hero-art" role="img" aria-label="Brand illustration of a bare foot with a fern" style="left:268px;top:33px;width:144px;height:166px;"></div>

    <p class="brand-name" style="left:455px;top:20px;font-size:27px;">BRAMBLE KEEP<sup>®</sup></p>
    <div class="rule" style="left:455px;top:54px;width:198px;"></div>
    <p class="product-main" style="left:453px;top:62px;font-size:50px;">RIDGE</p>
    <p class="product-main" style="left:453px;top:104px;font-size:50px;">MENDER</p>
    <p class="product-sub" style="left:453px;top:146px;font-size:36px;">BALM</p>
    <div class="tag-pill" style="left:448px;top:181px;width:213px;height:19px;">• FOR HARDWORKING SOLES •</div>
    <p class="net" style="left:459px;top:202px;">120ml ℮</p>

    <div class="origin-seal" role="img" aria-label="New Zealand sourced ingredients seal" style="left:711px;top:14px;width:82px;height:82px;"></div>

    <p class="body-copy justify" style="left:866px;top:20px;width:204px;font-size:11.3px;line-height:14.2px;"><span class="kicker" style="font-size:12px;">INGREDIENTS:</span> Shea Butter, Beef Tallow, Beeswax, Grape Seed Oil, Vegetable Glycerin, Lanolin, Panthenol, Gluconolactone, Sodium Benzoate, Allantoin, Manuka Honey, Vitamin E, Tea Tree Essential Oil, Lemon Myrtle Essential Oil, Rosemary Oleoresin Extract</p>
    <div class="brand-lockup" style="left:872px;top:122px;width:90px;">
      <span class="brand-dot" style="width:44px;height:44px;"></span>
      <span class="brand-word" style="font-size:14px;">BRAMBLE KEEP</span>
    </div>
    <div class="brand-column" style="left:960px;top:116px;width:100px;">
      <p class="maker">BRAMBLE KEEP NZ<small>Proudly made for hardworking Kiwis.</small></p>
      <div class="col-rule" style="margin:6px auto 0;width:70px;"></div>
      <div class="social-row" style="margin-top:8px;"><span></span><span></span><span></span></div>
      <p class="handle" style="margin-top:4px;">@bramblekeepnz</p>
      <p class="web" style="margin-top:8px;">www.bramblekeep.nz</p>
    </div>
  </section>

  <!-- OPTION 5 -->
  <h2 class="option-title" style="top:325px;">OPTION 5 <span class="option-note">Color pantone of the Bramble Keep logo</span></h2>
  <section class="label" style="top:362px;">
    <svg class="label-bg" viewBox="0 0 1080 227" aria-hidden="true">
      <path d="M235 0 C228 90 255 170 317 227 L620 227 C650 165 675 80 678 0 Z" fill="var(--clay)"/>
      <path d="M235 0 C228 90 255 170 317 227 L592 227 C625 165 650 80 660 0 Z" fill="var(--olive-dark)"/>
    </svg>
    <div class="fern-art" role="img" aria-label="Fern frond illustration" style="left:608px;top:85px;width:120px;height:142px;clip-path:polygon(88% 0,100% 8%,30% 100%,0 100%);"></div>

    <p class="kicker" style="left:27px;top:16px;">BUILT FOR HARDWORKING FEET</p>
    <p class="body-copy" style="left:27px;top:32px;width:186px;">Ridge Mender Balm is a no-nonsense formula that helps repair dry, cracked heels and tough, calloused skin. Made in New Zealand with premium 100% NZ sourced ingredients.</p>
    <div class="col-rule" style="left:27px;top:113px;width:182px;"></div>
    <div class="step" style="left:18px;top:128px;width:56px;">
      <svg class="step-icon" width="42" height="36" viewBox="0 0 42 36"><path d="M4 20 h34 l-3 12 h-28 z" fill="none" stroke="var(--ink)" stroke-width="1.4"/><path d="M12 8 q2 -3 0 -6 M17 8 q2 -3 0 -6 M22 8 q2 -3 0 -6" fill="none" stroke="var(--ink)" stroke-width="1.2"/></svg>
      <p class="step-name">SOAK</p>
      <p class="step-text">Soak feet in warm water</p>
    </div>
    <div class="step-divider" style="left:80px;top:127px;"></div>
    <div class="step" style="left:88px;top:128px;width:62px;">
      <svg class="step-icon" width="46" height="36" viewBox="0 0 46 36"><path d="M4 30 q10 -4 18 -14 l8 -10 M14 32 h24 q4 -4 -2 -8 l-10 0" fill="none" stroke="var(--ink)" stroke-width="1.4"/></svg>
      <p class="step-name">APPLY</p>
      <p class="step-text">Massage balm into heels</p>
    </div>
    <div class="step-divider" style="left:160px;top:127px;"></div>
    <div class="step" style="left:166px;top:128px;width:52px;">
      <svg class="step-icon" width="36" height="36" viewBox="0 0 36 36"><path d="M16 2 h10 v18 l-8 12 a5 5 0 0 1 -9 -5 l7 -9 z" fill="none" stroke="var(--ink)" stroke-width="1.4"/></svg>
      <p class="step-name">SOCKS</p>
      <p class="step-text">Wear socks overnight</p>
    </div>

    <div class="hero-art" role="img" aria-label="Brand illustration of a bare foot with a fern" style="left:277px;top:50px;width:114px;height:124px;"></div>

    <p class="brand-name" style="left:422px;top:14px;font-size:27px;">BRAMBLE KEEP<sup>®</sup></p>
    <div class="rule" style="left:405px;top:46px;width:236px;"></div>
    <p class="product-main" style="left:404px;top:52px;font-size:84px;">RIDGE</p>
    <p class="product-sub" style="left:404px;top:126px;font-size:41px;">MENDER BALM</p>
    <div class="tag-pill" style="left:404px;top:170px;width:205px;height:18px;">• FOR HARDWORKING SOLES •</div>
    <p class="net" style="left:409px;top:196px;font-size:16px;">120ml ℮</p>

    <div class="origin-seal" role="img" aria-label="New Zealand sourced ingredients seal" style="left:622px;top:20px;width:76px;height:76px;"></div>

    <p class="body-copy" style="left:732px;top:20px;width:212px;"><span class="kicker">DIRECTIONS:</span> Soak feet in warm water. Dry thoroughly. Massage a generous amount into heels. For results, use nightly and wear socks.</p>
    <div class="col-rule" style="left:732px;top:68px;width:210px;"></div>
    <p class="body-copy justify" style="left:732px;top:75px;width:210px;"><span class="kicker">INGREDIENTS:</span> Shea Butter, Beef Tallow, Beeswax, Grape Seed Oil, Vegetable Glycerin, Lanolin, Panthenol, Gluconolactone, Sodium Benzoate, Allantoin, Manuka Honey, Vitamin E, Tea Tree Essential Oil, Lemon Myrtle Essential Oil, Rosemary Oleoresin Extract</p>
    <div class="col-rule" style="left:732px;top:169px;width:210px;"></div>
    <p class="made-in" style="left:733px;top:186px;">MADE IN<br>NEW ZEALAND</p>
    <div class="pao" style="left:859px;top:184px;">6M</div>
    <svg class="recycle" style="left:908px;top:182px;" viewBox="0 0 28 26"><path d="M14 3 L25 22 L3 22 Z" fill="none" stroke="var(--ink)" stroke-width="1.6" stroke-dasharray="9 3"/></svg>

    <div class="col-vrule" style="left:959px;top:25px;height:180px;"></div>
    <div class="brand-column" style="left:964px;top:14px;width:104px;">
      <div class="brand-lockup"><span class="brand-dot"></span><span class="brand-word">BRAMBLE KEEP</span></div>
      <p class="maker" style="margin-top:14px;">BRAMBLE KEEP NZ<small>Proudly made for hardworking Kiwis.</small></p>
      <div class="col-rule" style="margin:6px auto 0;width:74px;"></div>
      <div class="social-row" style="margin-top:8px;"><span></span><span></span><span></span></div>
      <p class="handle" style="margin-top:5px;">@bramblekeepnz</p>
      <p class="web" style="margin-top:8px;">www.bramblekeep.nz</p>
    </div>
  </section>

  <!-- OPTION 6 -->
  <h2 class="option-title" style="top:619px;">OPTION 6 <span class="option-note">Color pantone of the Bramble Keep logo</span></h2>
  <section class="label" style="top:651px;">
    <svg class="label-bg" viewBox="0 0 1080 227" aria-hidden="true">
      <path d="M235 0 C228 90 255 170 317 227 L707 227 L707 0 Z" fill="var(--clay)"/>
      <path d="M250 0 C244 90 262 170 317 227 L707 227 L707 0 Z" fill="var(--olive-dark)"/>
    </svg>
    <div class="fern-art" role="img" aria-label="Fern frond illustration" style="left:605px;top:108px;width:95px;height:119px;clip-path:polygon(86% 0,100% 8%,30% 100%,0 100%);"></div>

    <p class="kicker" style="left:27px;top:16px;">BUILT FOR HARDWORKING FEET</p>
    <p class="body-copy" style="left:27px;top:32px;width:186px;">Ridge Mender Balm is a no-nonsense formula that helps repair dry, cracked heels and tough, calloused skin. Made in New Zealand with premium 100% NZ sourced ingredients.</p>
    <div class="col-rule" style="left:27px;top:113px;width:182px;"></div>
    <div class="step" style="left:18px;top:128px;width:56px;">
      <svg class="step-icon" width="42" height="36" viewBox="0 0 42 36"><path d="M4 20 h34 l-3 12 h-28 z" fill="none" stroke="var(--ink)" stroke-width="1.4"/><path d="M12 8 q2 -3 0 -6 M17 8 q2 -3 0 -6 M22 8 q2 -3 0 -6" fill="none" stroke="var(--ink)" stroke-width="1.2"/></svg>
      <p class="step-name">SOAK</p>
      <p class="step-text">Soak feet in warm water</p>
    </div>
    <div class="step-divider" style="left:80px;top:127px;"></div>
    <div class="step" style="left:88px;top:128px;width:62px;">
      <svg class="step-icon" width="46" height="36" viewBox="0 0 46 36"><path d="M4 30 q10 -4 18 -14 l8 -10 M14 32 h24 q4 -4 -2 -8 l-10 0" fill="none" stroke="var(--ink)" stroke-width="1.4"/></svg>
      <p class="step-name">APPLY</p>
      <p class="step-text">Massage balm into heels</p>
    </div>
    <div class="step-divider" style="left:160px;top:127px;"></div>
    <div class="step" style="left:166px;top:128px;width:52px;">
      <svg class="step-icon" width="36" height="36" viewBox="0 0 36 36"><path d="M16 2 h10 v18 l-8 12 a5 5 0 0 1 -9 -5 l7 -9 z" fill="none" stroke="var(--ink)" stroke-width="1.4"/></svg>
      <p class="step-name">SOCKS</p>
      <p class="step-text">Wear socks overnight</p>
    </div>

    <div class="hero-art" role="img" aria-label="Brand illustration of a bare foot with a fern" style="left:277px;top:50px;width:114px;height:124px;"></div>

    <p class="brand-name" style="left:422px;top:14px;font-size:27px;">BRAMBLE KEEP<sup>®</sup></p>
    <div class="rule" style="left:405px;top:46px;width:236px;"></div>
    <p class="product-main" style="left:404px;top:52px;font-size:84px;">RIDGE</p>
    <p class="product-sub" style="left:404px;top:126px;font-size:41px;">MENDER BALM</p>
    <div class="tag-pill" style="left:404px;top:170px;width:205px;height:18px;">• FOR HARDWORKING SOLES •</div>
    <p class="net" style="left:476px;top:196px;font-size:16px;">120ml ℮</p>

    <div class="origin-seal" role="img" aria-label="New Zealand sourced ingredients seal" style="left:616px;top:26px;width:76px;height:76px;"></div>

    <p class="body-copy" style="left:732px;top:20px;width:212px;"><span class="kicker">DIRECTIONS:</span> Soak feet in warm water. Dry thoroughly. Massage a generous amount into heels. For results, use nightly and wear socks.</p>
    <div class="col-rule" style="left:732px;top:68px;width:210px;"></div>
    <p class="body-copy justify" style="left:732px;top:75px;width:210px;"><span class="kicker">INGREDIENTS:</span> Shea Butter, Beef Tallow, Beeswax, Grape Seed Oil, Vegetable Glycerin, Lanolin, Panthenol, Gluconolactone, Sodium Benzoate, Allantoin, Manuka Honey, Vitamin E, Tea Tree Essential Oil, Lemon Myrtle Essential Oil, Rosemary Oleoresin Extract</p>
    <div class="col-rule" style="left:732px;top:169px;width:210px;"></div>
    <p class="made-in" style="left:733px;top:186px;">MADE IN<br>NEW ZEALAND</p>
    <div class="pao" style="left:817px;top:184px;">6M</div>
    <svg class="recycle" style="left:866px;top:182px;" viewBox="0 0 28 26"><path d="M14 3 L25 22 L3 22 Z" fill="none" stroke="var(--ink)" stroke-width="1.6" stroke-dasharray="9 3"/></svg>

    <div class="col-vrule" style="left:959px;top:25px;height:180px;"></div>
    <div class="brand-column" style="left:964px;top:14px;width:104px;">
      <div class="brand-lockup"><span class="brand-dot"></span><span class="brand-word">BRAMBLE KEEP</span></div>
      <p class="maker" style="margin-top:14px;">BRAMBLE KEEP NZ<small>Proudly made for hardworking Kiwis.</small></p>
      <div class="col-rule" style="margin:6px auto 0;width:74px;"></div>
      <div class="social-row" style="margin-top:8px;"><span></span><span></span><span></span></div>
      <p class="handle" style="margin-top:5px;">@bramblekeepnz</p>
      <p class="web" style="margin-top:8px;">www.bramblekeep.nz</p>
    </div>
  </section>

  <p class="footnote">Note: This artwork is designed in CMYK for printing. Colors may appear <b>slightly</b> different on screens.</p>
</main>
</body>
</html>
```